Pinecrest Rapids Outfitters
In the Spirit of Fun and Adventure
Pinecrest Rapids Outfitters - Travel
Creative Brief
Bright & Fun-filled
Dale Hartwin
38217 Sorrel Ln Ridgefold Crossing, MT. 59412
www.paddlevortex.example
info@paddlevortex.example
38217 Sorrel Ln
Our logo is fairly clean and simple but would like to add a fun whitewater element to the card to liven it up.
Add A : Join the Adventure on: Friendspace Logo Journey Scout logo Clip Stream Logo Chirpline Logo

```html
<!DOCTYPE html>
<html lang="en">
<head>
<meta charset="utf-8">
<title>Pinecrest Rapids Outfitters – Business Card</title>
<link rel="stylesheet" href="https://fonts.googleapis.com/css2?family=Open+Sans:wght@400;600;700&display=swap">
<style>
  :root {
    --backdrop: #e9e4dc;
    --card: #ffffff;
    --navy: #1d2f6b;
    --blue: #2a5db0;
    --sky: #6fa4dc;
    --text: #2b2b2b;
    --muted: #555b66;
    --rule: #b9bfca;
  }
  * { box-sizing: border-box; margin: 0; padding: 0; }
  html, body { width: 1200px; height: 451px; overflow: hidden; }
  body {
    background: var(--backdrop);
    font-family: "Open Sans", Arial, sans-serif;
    color: var(--text);
    position: relative;
  }
  .card {
    position: absolute;
    top: 84px;
    width: 532px;
    height: 288px;
    background: var(--card);
    border-radius: 18px;
    overflow: hidden;
  }
  .card--front { left: 43px; }
  .card--back { left: 620px; }

  .brand { display: flex; align-items: center; gap: 12px; }
  .brand__mark {
    width: 58px; height: 58px; border-radius: 50%;
    background: var(--blue); flex: none;
  }
  .brand__name {
    font-weight: 700; color: var(--navy);
    font-size: 21px; line-height: 1.05; text-transform: uppercase;
    letter-spacing: 0.5px; white-space: nowrap;
  }
  .card--front .brand { position: absolute; left: 44px; top: 34px; }

  .person { position: absolute; left: 40px; top: 148px; width: 220px; text-align: center; }
  .person__name { font-size: 20px; font-weight: 700; color: var(--navy); margin-bottom: 8px; }
  .person__address { font-size: 12px; line-height: 1.55; color: var(--muted); white-space: nowrap; }

  .divider {
    position: absolute; left: 268px; top: 102px; width: 1px; height: 110px;
    background: var(--rule);
  }
  .contacts { position: absolute; left: 282px; top: 100px; list-style: none; }
  .contacts li {
    display: flex; align-items: center; gap: 8px;
    font-size: 12px; color: var(--muted); height: 22px; white-space: nowrap;
  }
  .contacts svg { width: 12px; height: 12px; fill: var(--navy); flex: none; }

  .wave { position: absolute; left: 0; bottom: 0; width: 532px; height: 80px; }

  .card--back .brand {
    position: absolute; left: 50%; top: 62px; transform: translateX(-50%);
  }
  .social { position: absolute; left: 56px; top: 172px; width: 420px; }
  .social__title {
    font-size: 14px; font-weight: 700; color: var(--navy);
    text-align: center; margin-bottom: 14px; padding-left: 40px;
  }
  .social__grid {
    list-style: none; display: grid;
    grid-template-columns: 200px 200px; column-gap: 20px;
    row-gap: 14px; padding-left: 30px;
  }
  .social__grid li {
    display: flex; align-items: center; gap: 8px;
    font-size: 12px; color: var(--muted); white-space: nowrap;
  }
  .social__dot { width: 18px; height: 18px; border-radius: 3px; background: var(--blue); flex: none; }
</style>
</head>
<body>
  <section class="card card--front" aria-label="Business card front">
    <div class="brand">
      <span class="brand__mark"></span>
      <span class="brand__name">Pinecrest<br>Rapids<br>Outfitters</span>
    </div>

    <div class="person">
      <p class="person__name">Dale Hartwin</p>
      <p class="person__address">38217 Sorrel Ln<br>Ridgefold Crossing, MT. 59412</p>
    </div>

    <span class="divider"></span>

    <ul class="contacts">
      <li><svg viewBox="0 0 12 12"><path d="M3 1l2 2-1 2c1 1.5 2 2.5 3 3l2-1 2 2-1.5 2C5 11 1 7 1 2.5z"/></svg>(T) 8005550142</li>
      <li><svg viewBox="0 0 12 12"><path d="M3 1l2 2-1 2c1 1.5 2 2.5 3 3l2-1 2 2-1.5 2C5 11 1 7 1 2.5z"/></svg>4065550187</li>
      <li><svg viewBox="0 0 12 12"><path d="M3 1l2 2-1 2c1 1.5 2 2.5 3 3l2-1 2 2-1.5 2C5 11 1 7 1 2.5z"/></svg>4065550163</li>
      <li><svg viewBox="0 0 12 12"><circle cx="6" cy="6" r="5" fill="none" stroke="#1d2f6b" stroke-width="1.6"/><circle cx="6" cy="6" r="2"/></svg>info@paddlevortex.example</li>
      <li><svg viewBox="0 0 12 12"><circle cx="6" cy="6" r="5" fill="none" stroke="#1d2f6b" stroke-width="1.4"/><path d="M1 6h10M6 1c2 2 2 8 0 10M6 1c-2 2-2 8 0 10" fill="none" stroke="#1d2f6b" stroke-width="1"/></svg>www.paddlevortex.example</li>
    </ul>

    <svg class="wave" viewBox="0 0 532 80" preserveAspectRatio="none" aria-hidden="true">
      <path d="M0 40 C120 70 260 70 380 40 S500 10 532 18 V80 H0z" fill="var(--sky)"/>
      <path d="M0 58 C140 80 280 74 400 50 S510 30 532 34 V80 H0z" fill="var(--blue)"/>
      <path d="M0 70 C160 86 300 80 420 64 S515 54 532 56 V80 H0z" fill="var(--navy)"/>
    </svg>
  </section>

  <section class="card card--back" aria-label="Business card back">
    <div class="brand">
      <span class="brand__mark"></span>
      <span class="brand__name">Pinecrest<br>Rapids<br>Outfitters</span>
    </div>

    <div class="social">
      <p class="social__title">Join the Adventure on :</p>
      <ul class="social__grid">
        <li><span class="social__dot"></span>Friendspace@paddlevortex</li>
        <li><span class="social__dot"></span>clipstream@paddlevortex</li>
        <li><span class="social__dot"></span>Chirpline@paddlevortex</li>
        <li><span class="social__dot"></span>Journey Scout@paddlevortex</li>
      </ul>
    </div>
  </section>
</body>
</html>
```